Broschüre für Sicherheitsdienstleistungen
Zielgruppe
Sicherheitsunternehmen
Hallo,
Wir möchten gerne eine Broschüre (ca. 12 Seiten) gestalten lassen wo alle unsere verschiedene Dienstleistungen Beschrieben werden und unser unternehmen vorgestellt wird an den Kunden.
Als Hard copy Version von unsere neue Seite : http://kwt.seitenplanung-beispiel.de
Das Design soll Freundlich und Modern Gestaltet werden.
Farbtöne gerne in Weiss und Dunkel Blau
Produktdetails :
Rückendrahtheftung links, 4/4-farbig (beidseitiger Druck, CMYK)
ab 250 g wird der Umschlag zusätzlich genutet
Veredelung Umschlag
beidseitiger UV-Lack glänzend
Format
DIN A4 (21 x 29,7 cm)
Details: Hochformat
Seitenanzahl ca. 10 - 12 (Excl. Umschlag)
Material Umschlag
250g Bilderdruck glänzend
New Website Design :
http://kwt.seitenplanung-beispiel.de

```html
<!DOCTYPE html>
<html lang="de">
<head>
<meta charset="utf-8">
<title>KWT SECURA – Broschüre Sicherheitsdienst</title>
<link href="https://fonts.googleapis.com/css2?family=Open+Sans:wght@400;700&family=Roboto+Condensed:wght@400;700&display=swap" rel="stylesheet">
<style>
:root{
  --bg:#e3e3e3;
  --rule:#d2d2d2;
  --paper:#ffffff;
  --navy:#1f3f5e;
  --text:#3d4650;
  --band:#eef1f4;
}
*{margin:0;padding:0;box-sizing:border-box}
html,body{width:1200px;height:5038px;overflow:hidden;background:var(--bg)}
body{font-family:"Open Sans",Arial,sans-serif;color:var(--text)}
.section{position:relative;width:1200px;height:840px;border-bottom:1px solid var(--rule)}
.section:last-child{height:838px;border-bottom:none}

.brand-mark{position:absolute;left:86px;top:110px;display:flex;align-items:center;gap:10px;
  font-family:"Roboto Condensed",Arial,sans-serif;font-weight:700;font-size:28px;color:#fff;letter-spacing:1px}
.brand-mark .dot{width:22px;height:22px;border-radius:50%;background:#fff}

.cover{position:absolute;left:410px;top:110px;width:400px;height:560px;
  box-shadow:0 12px 30px rgba(0,0,0,.22);overflow:hidden}
.cover .photo{position:absolute;inset:0;background:
  radial-gradient(ellipse 60% 18% at 55% 10%,rgba(30,20,15,.85),transparent 70%),
  radial-gradient(circle at 50% 30%,#ffd88a 0%,rgba(255,190,100,.6) 18%,transparent 45%),
  linear-gradient(180deg,#e9a24c 0%,#d07a34 28%,#9a5a2e 52%,#6b4029 72%,#3e2618 100%)}
.cover .cover-brand{position:absolute;left:0;right:0;top:215px;display:flex;justify-content:center;align-items:center;gap:8px;
  font-family:"Roboto Condensed",Arial,sans-serif;font-weight:700;font-size:20px;color:#fff;letter-spacing:1px}
.cover .cover-brand .dot{width:14px;height:14px;border-radius:50%;background:#fff}
.cover .cover-title{position:absolute;left:0;right:0;top:310px;text-align:center;
  font-family:"Roboto Condensed",Arial,sans-serif;font-weight:700;font-size:34px;line-height:1.1;color:#fff;letter-spacing:3px}
.cover .cover-url{position:absolute;left:0;right:0;top:420px;text-align:center;font-size:14px;color:#fff}

.spread{position:absolute;left:200px;top:137px;width:800px;height:566px;display:flex;
  box-shadow:0 12px 30px rgba(0,0,0,.2)}
.page{position:relative;width:400px;height:566px;background:var(--paper);overflow:hidden}
.page.left{box-shadow:inset -14px 0 18px -14px rgba(0,0,0,.18)}
.page.right{box-shadow:inset 14px 0 18px -14px rgba(0,0,0,.18)}
.photo-fill{position:absolute;inset:0}
.vertical-label{position:absolute;left:12px;bottom:18px;writing-mode:vertical-rl;transform:rotate(180deg);
  white-space:nowrap;font-family:"Roboto Condensed",Arial,sans-serif;font-size:36px;color:rgba(255,255,255,.9);letter-spacing:1px}
.vertical-label.right-side{left:auto;right:12px;bottom:auto;top:18px;transform:none}
.badge{position:absolute;width:96px;height:96px;border-radius:50%;background:var(--navy);color:#fff;
  display:flex;flex-direction:column;align-items:center;justify-content:center;text-align:center;
  font-family:"Roboto Condensed",Arial,sans-serif}
.badge .small{font-size:8px;line-height:1.3}
.badge .phone{font-size:11px;font-weight:700;margin-top:3px}
.badge.claim{font-weight:700;font-size:13px;line-height:1.15}
.overlay-claim{position:absolute;font-family:"Roboto Condensed",Arial,sans-serif;font-weight:700;font-size:16px;line-height:1.15;color:#fff}

.page-num{position:absolute;top:24px;width:14px;height:14px;background:var(--navy);color:#fff;font-size:7px;
  display:flex;align-items:center;justify-content:center}
.page.right .page-num{right:22px}
.page.left .page-num{left:22px}
.content{position:absolute;left:32px;right:32px;top:30px;bottom:26px}
.page-title{font-family:"Roboto Condensed",Arial,sans-serif;font-weight:700;font-size:15px;line-height:1.2;color:var(--navy);margin-right:24px}
.page.left .page-title{margin-left:24px;margin-right:0}
.intro{font-size:6.4px;line-height:1.5;margin-top:7px;text-align:justify}
.lead{margin:9px -32px 0;padding:7px 32px;background:var(--band);font-family:"Roboto Condensed",Arial,sans-serif;font-weight:700;
  font-size:6.5px;line-height:1.45;color:var(--navy);letter-spacing:.4px;text-transform:uppercase}
.columns{column-count:3;column-gap:12px;margin-top:11px;font-size:5.6px;line-height:1.55;text-align:justify;hyphens:auto}
.columns.two{column-count:2;column-gap:16px;font-size:5.9px}
.columns h3{font-family:"Roboto Condensed",Arial,sans-serif;font-weight:700;font-size:6.3px;color:var(--navy);text-transform:uppercase;margin:6px 0 2px;line-height:1.25;text-align:left}
.columns h3:first-child{margin-top:0}
.columns p{margin-bottom:3px}
</style>
</head>
<body>

<section class="section cover-section">
  <div class="brand-mark"><span class="dot"></span>KWT SECURA</div>
  <div class="cover">
    <div class="photo" role="img" aria-label="Drohne vor Sonnenuntergang über einer Stadt"></div>
    <div class="cover-brand"><span class="dot"></span>KWT SECURA</div>
    <div class="cover-title">IHR PROFESSIONELLER<br>SICHERHEITSDIENST</div>
    <div class="cover-url">kwt.seitenplanung-beispiel.de</div>
  </div>
</section>

<section class="section">
  <div class="spread">
    <div class="page left">
      <div class="photo-fill" role="img" aria-label="Zwei Kinder in Ritterkostümen auf einer grünen Wiese" style="background:
        radial-gradient(ellipse 30% 40% at 62% 55%,rgba(200,40,40,.75),transparent 70%),
        radial-gradient(ellipse 25% 35% at 32% 70%,rgba(230,225,210,.8),transparent 70%),
        radial-gradient(circle at 70% 25%,rgba(160,160,160,.7),transparent 30%),
        linear-gradient(165deg,#d6dd8a 0%,#9fb45a 25%,#5f7d34 55%,#3f5a2a 100%)"></div>
      <div class="vertical-label">KWT SEITENPLANUNG</div>
      <div class="badge claim" style="left:170px;top:50px">EINE<br>FRAGE DES<br>VERTRAUENS</div>
    </div>
    <div class="page right">
      <div class="page-num">3</div>
      <div class="content">
        <h2 class="page-title">DIE KWT SECURA GMBH<br>IHR PROFESSIONELLER SICHERHEITSDIENST</h2>
        <p class="intro">Viele Unternehmen bieten Ihnen Leistungen, die Sie nicht benötigen – der Service der KWT SECURA ist hingegen für jeden wichtig. Wir bieten Ihnen Sicherheit. Von Ihrem professionellen Sicherheitsdienst erhalten Sie maßgeschneiderte Konzepte, die Sie, Ihr Objekt oder Projekt langfristig schützen.</p>
        <p class="lead">Aufgrund der außergewöhnlichen Organisationsstruktur ist es uns möglich, in äußerster Weise flexibel und schnell zu agieren. Der Kunde entscheidet über den Umfang und die Schwerpunkte des Einsatzes.</p>
        <div class="columns">
          <h3>Geschützt für Deutschland und darüber hinaus</h3>
          <p>Die KWT SECURA, der professionelle Sicherheitsdienst mit Sitz in Düsseldorf, gibt Ihnen umfassenden Schutz. Als Profis im Bereich des Sicherheitsmanagements bieten wir Ihnen die Umsetzung einer vollständigen Planung. Wir schützen Privatpersonen, Gebäude und Firmen und sorgen dafür, dass Ihre Veranstaltung ohne Zwischenfälle abläuft. Gleichzeitig sind wir bei besonderen Einsätzen im Ausland tätig und arbeiten nach festen Standards.</p>
          <h3>Eine Frage des Vertrauens – wer sind wir?</h3>
          <p>Die KWT SECURA GmbH wurde gegründet, um Ihnen einen verlässlichen Partner an die Seite zu stellen. Unser Team bringt langjährige Erfahrung mit und wird regelmäßig geschult. Vertrauen, Diskretion und Zuverlässigkeit bilden die Grundlage jeder Zusammenarbeit. Wir hören zu, planen gemeinsam und handeln verantwortungsvoll, damit Sie sich ganz auf Ihre Aufgaben konzentrieren können.</p>
          <p>Zudem arbeiten unsere Mitarbeiter mit moderner technischer Ausrüstung, etwa Funk, Kameras und Drohnen, die wir gezielt einsetzen.</p>
          <h3>Sicherer Schutz in vielen Bereichen</h3>
          <p>Die KWT SECURA GmbH ist als Sicherheitsdienst in vielen Bereichen tätig. Sie beauftragen uns als professionellen Personenschutz, zur Bewachung von Objekten, als Fahrdienst oder für maritime Einsätze. Unsere Teams begleiten Sie auf Reisen und sichern Veranstaltungen, Baustellen, Lager und Büroflächen zuverlässig ab.</p>
          <h3>Der flexible und professionelle Sicherheitsdienst</h3>
          <p>Aufgrund unserer schlanken Organisationsstruktur können wir schnell reagieren und den Einsatz jederzeit an Ihre Wünsche anpassen. Kurze Wege und klare Absprachen machen uns zu einem beweglichen Partner.</p>
          <p>Im Kundengespräch ermitteln wir den genauen Bedarf, erstellen ein passendes Konzept und stellen das richtige Team zusammen. So erhalten Sie genau den Schutz, den Sie benötigen, ohne unnötige Zusatzkosten.</p>
          <h3>Auf der sicheren Seite mit der KWT SECURA</h3>
          <p>Die KWT SECURA ist Ihr Sicherheitsdienst für Deutschland und darüber hinaus. Gerne beraten wir Sie unverbindlich und individuell. Vereinbaren Sie einfach einen Termin unter 0800 / 000 1234 – wir freuen uns auf Ihre Anfrage.</p>
        </div>
      </div>
    </div>
  </div>
</section>

<section class="section">
  <div class="spread">
    <div class="page left">
      <div class="page-num">4</div>
      <div class="content">
        <h2 class="page-title">KWT SECURA – DER PROFESSIONELLE PERSONENSCHUTZ</h2>
        <p class="intro">Die KWT SECURA GmbH ist Ihr erfahrener Partner im Bereich Personenschutz. Diskret, aufmerksam und stets vorbereitet begleiten wir Sie im Alltag, bei Terminen und auf Reisen. Ihre Sicherheit steht für uns an erster Stelle.</p>
        <div class="columns">
          <h3>Persönlicher Schutz, individuell geplant</h3>
          <p>Jeder Auftrag beginnt mit einer genauen Analyse der Lage und Ihrer Wünsche. Wir prüfen mögliche Risiken, planen Wege und Abläufe und stimmen jeden Schritt mit Ihnen ab. So entsteht ein Schutzkonzept, das zu Ihrem Leben passt und Sie nicht einschränkt.</p>
          <h3>Erfahrene Personenschützer</h3>
          <p>Unser Team bringt langjährige Erfahrung und regelmäßige Schulungen mit. Unsere Personenschützer sind körperlich fit, sprachgewandt und geübt im Umgang mit schwierigen Situationen. Sie handeln ruhig, überlegt und entschlossen.</p>
          <h3>Schutz im In- und Ausland</h3>
          <p>Wir begleiten Sie weltweit und koordinieren alle Abläufe vor Ort. Ob Geschäftsreise, Messe oder privater Aufenthalt – wir kümmern uns um Unterkunft, Transport und die Abstimmung mit lokalen Partnern.</p>
          <h3>Diskretion als Grundsatz</h3>
          <p>Ihre Privatsphäre bleibt gewahrt, unser Einsatz bleibt unauffällig. Unsere Mitarbeiter passen sich Ihrem Umfeld an und treten nur dann in Erscheinung, wenn es wirklich notwendig ist. Vertraulichkeit gilt für jede Information.</p>
          <h3>Schutz für Familien und Kinder</h3>
          <p>Auch Angehörige verdienen Sicherheit. Wir begleiten Kinder zur Schule, sichern Familienfeiern und sind für Ihre Liebsten da, wenn Sie selbst unterwegs sind.</p>
          <h3>Begleitung bei Veranstaltungen</h3>
          <p>Bei öffentlichen Auftritten, Empfängen und Konferenzen sorgen wir für geordnete Abläufe, kontrollieren Zugänge und halten Abstand zu unerwünschten Personen.</p>
          <h3>Ihr Kontakt zur KWT SECURA</h3>
          <p>Gerne beraten wir Sie persönlich und erstellen ein passendes Angebot. Rufen Sie uns an oder schreiben Sie uns – wir melden uns schnell bei Ihnen und besprechen alle Details in Ruhe.</p>
        </div>
      </div>
    </div>
    <div class="page right">
      <div class="photo-fill" role="img" aria-label="Junge Frau mit Krone zwischen zwei Rittern in Rüstung im Grünen" style="background:
        radial-gradient(ellipse 22% 30% at 50% 68%,rgba(200,30,30,.8),transparent 70%),
        radial-gradient(ellipse 40% 35% at 50% 80%,rgba(225,215,195,.85),transparent 70%),
        radial-gradient(ellipse 14% 22% at 18% 62%,rgba(70,80,90,.9),transparent 70%),
        radial-gradient(ellipse 14% 22% at 84% 66%,rgba(70,80,90,.9),transparent 70%),
        linear-gradient(175deg,#b7c870 0%,#7d9a44 35%,#4f6a2c 65%,#3a4a2a 100%)"></div>
      <div class="overlay-claim" style="left:60px;top:70px">DAS TEAM DER<br>KWT SECURA<br>SCHÜTZT SIE<br>ZUVERLÄSSIG.</div>
      <div class="badge" style="left:270px;top:40px"><span class="small">Jetzt Beratungstermin<br>vereinbaren unter:</span><span class="phone">0800 / 000 1234</span></div>
    </div>
  </div>
</section>

<section class="section">
  <div class="spread">
    <div class="page left">
      <div class="photo-fill" role="img" aria-label="Containerschiff im beleuchteten Hafen bei Abenddämmerung" style="background:
        radial-gradient(ellipse 50% 10% at 45% 48%,rgba(240,170,80,.8),transparent 70%),
        radial-gradient(ellipse 60% 14% at 55% 62%,rgba(230,150,60,.55),transparent 70%),
        linear-gradient(180deg,#2a66a0 0%,#4f8cc2 30%,#7a90a6 44%,#3b4d63 56%,#2a3a4e 75%,#1a2533 100%)"></div>
      <div class="vertical-label">KWT SEITENPLANUNG</div>
      <div class="badge" style="left:150px;top:30px"><span class="small">Jetzt Beratungstermin<br>vereinbaren unter:</span><span class="phone">0800 / 000 1234</span></div>
    </div>
    <div class="page right">
      <div class="page-num">5</div>
      <div class="content">
        <h2 class="page-title">KWT SECURA – IHR SICHERHEITSUNTERNEHMEN FÜR HIGH RISK SECURITY UND MARITIME SICHERHEIT</h2>
        <p class="intro">Die KWT SECURA GmbH ist Ihr Partner für Einsätze in besonders sensiblen Regionen und auf See. Wir schützen Besatzung, Fracht und Schiff und sorgen dafür, dass Ihre Projekte auch unter schwierigen Bedingungen sicher ablaufen.</p>
        <div class="columns two">
          <h3>Wir sind für Sie da</h3>
          <p>Unsere Teams arbeiten nach klaren Standards und stimmen jeden Schritt mit Ihnen ab. Vor jedem Einsatz erstellen wir eine genaue Lageeinschätzung und entwickeln daraus einen Plan, der alle Beteiligten einbezieht.</p>
          <h3>Maritime Sicherheit auf allen Routen</h3>
          <p>Wir begleiten Handelsschiffe durch Gebiete mit erhöhtem Risiko und sichern Häfen und Terminals. Unsere Mitarbeiter sind für den Einsatz an Bord ausgebildet und arbeiten eng mit Kapitän und Besatzung zusammen. So bleiben Route, Ladung und Mannschaft geschützt.</p>
          <h3>High Risk Security mit Erfahrung</h3>
          <p>Für Projekte in Krisenregionen planen wir Schutz, Logistik und Kommunikation aus einer Hand. Wir kennen die Anforderungen vor Ort und arbeiten mit verlässlichen Partnern zusammen, damit Ihr Vorhaben wie geplant umgesetzt werden kann.</p>
          <h3>Beratung und Risikoanalyse</h3>
          <p>Bevor ein Einsatz beginnt, analysieren wir die Lage gründlich. Wir bewerten Gefahren, prüfen Abläufe und geben klare Empfehlungen. Auf dieser Grundlage treffen Sie fundierte Entscheidungen.</p>
          <h3>Schnell einsatzbereit</h3>
          <p>Kurze Reaktionszeiten und ein eingespieltes Team sind unsere Stärke. Auch kurzfristige Anfragen setzen wir zuverlässig um.</p>
          <h3>Sicherheitsleistungen für High Risk Security, Maritime Sicherheit und mehr</h3>
          <p>Sprechen Sie uns an – gemeinsam finden wir die passende Lösung für Ihre Anforderungen und begleiten Sie vom ersten Gespräch bis zum Abschluss des Einsatzes.</p>
        </div>
      </div>
    </div>
  </div>
</section>

<section class="section">
  <div class="spread">
    <div class="page left">
      <div class="page-num">6</div>
      <div class="content">
        <h2 class="page-title">DER ZUVERLÄSSIGE FAHRDIENST</h2>
        <p class="intro">Sicher ankommen: Unser Fahrdienst bringt Sie pünktlich und geschützt an Ihr Ziel – ob Geschäftstermin, Flughafen, Hotel oder Veranstaltung. Lehnen Sie sich zurück, wir übernehmen den Rest.</p>
        <div class="columns">
          <h3>Geschulte Fahrer für Ihre Sicherheit</h3>
          <p>Unsere Fahrer sind im defensiven und sicheren Fahren ausgebildet und kennen die Strecken genau. Sie erkennen Gefahren früh, reagieren besonnen und bringen Sie ruhig und entspannt ans Ziel.</p>
          <h3>Moderne Fahrzeuge</h3>
          <p>Gepflegte Limousinen und Vans stehen für jeden Anlass bereit. Alle Fahrzeuge werden regelmäßig gewartet und sind komfortabel ausgestattet, damit Sie unterwegs arbeiten oder sich erholen können.</p>
          <h3>Pünktlichkeit und Diskretion</h3>
          <p>Wir planen Routen vorausschauend, berücksichtigen Verkehr und Baustellen und behandeln Ihre Termine vertraulich. Gespräche im Fahrzeug bleiben unter uns.</p>
          <h3>Flughafen- und Hoteltransfer</h3>
          <p>Wir holen Sie und Ihre Gäste ab, kümmern uns um das Gepäck und bringen alle sicher zur Unterkunft oder zum nächsten Termin.</p>
          <h3>Fahrdienst mit Personenschutz</h3>
          <p>Auf Wunsch kombinieren wir den Fahrdienst mit Personenschutz. So sind Sie auch beim Ein- und Aussteigen und vor Ort bestens begleitet.</p>
          <h3>Flexibel buchbar</h3>
          <p>Einzelfahrten oder dauerhafte Begleitung – Sie entscheiden den Umfang. Wir richten uns nach Ihrem Kalender, auch abends und am Wochenende.</p>
          <h3>Jetzt Fahrt anfragen</h3>
          <p>Rufen Sie uns an, wir beraten Sie gerne und erstellen Ihnen ein unverbindliches Angebot.</p>
        </div>
      </div>
    </div>
    <div class="page right">
      <div class="photo-fill" role="img" aria-label="Frau mit Kopfhörern auf dem Rücksitz eines Autos" style="background:
        radial-gradient(ellipse 30% 40% at 55% 45%,rgba(240,200,150,.85),transparent 70%),
        radial-gradient(ellipse 22% 24% at 48% 72%,rgba(170,40,50,.75),transparent 70%),
        linear-gradient(200deg,#5a2a4a 0%,#8a3a3e 30%,#c9865a 55%,#7a5a50 78%,#4a3a3a 100%)"></div>
      <div class="vertical-label right-side">KWT SEITENPLANUNG</div>
      <div class="badge" style="left:16px;top:60px"><span class="small">Jetzt Beratungstermin<br>vereinbaren unter:</span><span class="phone">0800 / 000 1234</span></div>
    </div>
  </div>
</section>

<section class="section">
  <div class="spread">
    <div class="page left">
      <div class="photo-fill" role="img" aria-label="Überwachungskamera über einem Parkplatz mit Bäumen und Gebäuden" style="background:
        radial-gradient(ellipse 30% 22% at 30% 75%,rgba(200,200,205,.9),transparent 70%),
        radial-gradient(ellipse 40% 20% at 65% 62%,rgba(110,140,80,.8),transparent 70%),
        linear-gradient(175deg,#e6ebef 0%,#b8c2ca 28%,#8c9aa4 45%,#6f8a5a 65%,#4a5a4a 100%)"></div>
      <div class="vertical-label">KWT SEITENPLANUNG</div>
      <div class="badge" style="left:150px;top:40px"><span class="small">Jetzt Beratungstermin<br>vereinbaren unter:</span><span class="phone">0800 / 000 1234</span></div>
    </div>
    <div class="page right">
      <div class="page-num">7</div>
      <div class="content">
        <h2 class="page-title">KWT SECURA – DER ZUVERLÄSSIGE OBJEKTSCHUTZ</h2>
        <p class="intro">Ob Bürogebäude, Baustelle, Lager oder Wohnanlage: Wir sichern Ihr Objekt rund um die Uhr und reagieren sofort, wenn es darauf ankommt. Mit einem durchdachten Konzept schützen wir Werte, Menschen und Abläufe.</p>
        <div class="columns two">
          <h3>Bewachung vor Ort</h3>
          <p>Unsere Mitarbeiter kontrollieren Zugänge, führen regelmäßige Rundgänge durch und dokumentieren jede Auffälligkeit. Ihre sichtbare Präsenz schreckt ungebetene Gäste ab und sorgt für ein gutes Gefühl bei Mitarbeitern und Besuchern.</p>
          <h3>Technische Überwachung</h3>
          <p>Kameras, Bewegungsmelder und Alarmanlagen ergänzen den Einsatz unserer Teams sinnvoll. Wir beraten Sie bei der Auswahl der Technik und verbinden sie mit klaren Abläufen im Alarmfall.</p>
          <h3>Empfangs- und Pfortendienst</h3>
          <p>Freundlich und aufmerksam empfangen wir Ihre Besucher und Lieferanten, vergeben Ausweise und behalten den Überblick, wer sich im Gebäude aufhält.</p>
          <h3>Baustellen- und Revierdienst</h3>
          <p>Wir schützen Maschinen und Material vor Diebstahl und Beschädigung. Im Revierdienst kontrollieren wir mehrere Objekte zu wechselnden Zeiten.</p>
          <h3>Ihr fester Ansprechpartner</h3>
          <p>Ein fester Kontakt begleitet Ihr Projekt von Anfang an. Er kennt Ihr Objekt, Ihre Wünsche und ist jederzeit für Sie erreichbar.</p>
          <h3>Objektschutz nach Maß</h3>
          <p>Vereinbaren Sie einen Termin – wir besichtigen Ihr Objekt und erstellen ein Angebot, das genau zu Ihnen passt.</p>
        </div>
      </div>
    </div>
  </div>
</section>

</body>
</html>
```